Ridgely Forge business card for handing simple contact information and generating service awareness

Utilizing the attached logo(s), generate a professional, but approachable, card conveying a sense of capability and integrity. Please only use one logo of the four attached; the different colors are all acceptable, but preference will be given to a design integrating a teal/turquoise logo,

I do not know where to put in the contact information or details?

Target Market(s)

Agriculture, Farming, Timber, Forestry, Construction, Crane Service

Industry/Entity Type

Contact Information for Business Card

Name, Phone Number, email address

Colors

Designer to choose colors to be used in the design.

Requirements
Nice to have
• It would be great to have either a mountain or one of the attached cranes as a backdrop on the rear of the card. Simple watermarks and/or Debossing is also great

```html
<!DOCTYPE html>
<html lang="en">
<head>
<meta charset="utf-8">
<title>Ridgely Forge — Business Card</title>
<link href="https://fonts.googleapis.com/css2?family=Arimo:wght@400;700&display=swap" rel="stylesheet">
<style>
  :root {
    --teal: #2d6f64;
    --ink: #1b1b1b;
    --paper: #ffffff;
    --backdrop: #e9eaeb;
  }
  * { margin: 0; padding: 0; box-sizing: border-box; }
  html, body {
    width: 1200px;
    height: 1000px;
    overflow: hidden;
    background: var(--backdrop);
    font-family: "Arimo", Arial, sans-serif;
  }
  .card {
    position: absolute;
    left: 303px;
    width: 593px;
    height: 338px;
  }
  .card-front { top: 108px; background: var(--paper); color: var(--ink); }
  .card-back { top: 552px; background: var(--teal); }

  .person-name {
    position: absolute;
    left: 43px;
    top: 40px;
    font-size: 31px;
    font-weight: 700;
    color: var(--teal);
    letter-spacing: 0.2px;
  }
  .person-title {
    position: absolute;
    left: 43px;
    top: 74px;
    font-size: 16px;
  }
  .address {
    position: absolute;
    left: 43px;
    top: 168px;
    font-size: 16px;
    line-height: 22px;
  }
  .phone, .email {
    position: absolute;
    left: 43px;
    font-size: 15px;
  }
  .phone { top: 236px; }
  .email { top: 262px; }
  .rule {
    position: absolute;
    left: 0;
    top: 290px;
    width: 381px;
    height: 2px;
    background: var(--teal);
  }
  .website {
    position: absolute;
    left: 390px;
    top: 282px;
    font-size: 14.5px;
  }

  .brand {
    position: absolute;
    display: flex;
    flex-direction: column;
    align-items: center;
    font-weight: 700;
  }
  .brand-front {
    left: 355px;
    top: 48px;
    width: 200px;
    color: var(--teal);
    font-size: 24px;
    gap: 14px;
  }
  .brand-front .brand-mark {
    width: 86px; height: 86px; border-radius: 50%;
    background: var(--teal);
  }
  .brand-back {
    left: 0;
    top: 50px;
    width: 100%;
    color: var(--paper);
    font-size: 40px;
    gap: 22px;
  }
  .brand-back .brand-mark {
    width: 160px; height: 160px; border-radius: 50%;
    background: var(--paper);
  }
</style>
</head>
<body>
  <section class="card card-front">
    <h1 class="person-name">SAMPLE NAME</h1>
    <p class="person-title">CEO/Founder</p>
    <p class="address">123 Street Name, Suite 456<br>Country Name, State 78901</p>
    <p class="phone">123-456-7890</p>
    <p class="email">samplename@ridgelyforge.com</p>
    <div class="rule"></div>
    <p class="website">www.websitename.com</p>
    <div class="brand brand-front">
      <span class="brand-mark"></span>
      <span class="brand-name">Ridgely Forge</span>
    </div>
  </section>

  <section class="card card-back">
    <div class="brand brand-back">
      <span class="brand-mark"></span>
      <span class="brand-name">Ridgely Forge</span>
    </div>
  </section>
</body>
</html>
```